Letterhead Design Project

Sunmark Growth Coaching Services

My info is
Daryna Feltwick-Osbourne
daryna@sunmarkgrowthco.com
sunmarkgrowthco.com
555-314-7720

you can play with order of items. I've never had a letterhead before. Thank you!

```html
<!DOCTYPE html>
<html lang="en">
<head>
<meta charset="utf-8">
<title>Sunmark Growth Coaching Services — Letterhead</title>
<link href="https://fonts.googleapis.com/css2?family=Roboto+Condensed:wght@400;700&display=swap" rel="stylesheet">
<style>
  :root {
    --backdrop: #353535;
    --paper: #ffffff;
    --orange: #f7941d;
    --red: #be1e2d;
    --ink: #58595b;
    --rule: #6d6e71;
    --faint: #ededed;
    --faint-ring: #e4e4e4;
  }
  * { margin: 0; padding: 0; box-sizing: border-box; }
  html, body {
    width: 879px; height: 1200px; overflow: hidden;
    background: var(--backdrop);
    font-family: "Roboto Condensed", Arial, sans-serif;
  }
  .stage { position: relative; width: 879px; height: 1200px; }
  .letterhead {
    position: absolute; left: 89px; top: 121px;
    width: 594px; height: 838px;
    background: var(--paper);
    transform: scale(1.1717); transform-origin: 0 0;
    overflow: hidden;
  }
  .header-shapes { position: absolute; left: 0; top: 0; }
  .brand {
    position: absolute; left: 40px; top: 22px; width: 230px;
    text-align: center; color: var(--red); font-weight: 700;
  }
  .brand-mark {
    display: block; width: 78px; height: 78px; margin: 0 auto 10px;
    border-radius: 50%; background: var(--orange);
    box-shadow: 0 0 0 3px var(--paper), 0 0 0 4px var(--red);
  }
  .brand-name { display: block; font-size: 31px; line-height: 1; }
  .brand-tag {
    display: block; font-size: 13px; letter-spacing: 3.2px;
    margin-top: 6px; text-transform: uppercase;
  }
  .contact {
    position: absolute; left: 358px; top: 58px;
    color: var(--paper); font-weight: 700; font-size: 14px; line-height: 16.8px;
  }
  .date-field {
    position: absolute; left: 335px; top: 145px;
    display: flex; align-items: flex-end;
  }
  .date-label {
    background: var(--red); color: var(--paper);
    font-weight: 700; font-size: 13px; line-height: 17px;
    padding: 0 6px 0 22px; height: 17px;
    clip-path: polygon(0 0, 100% 0, 100% 100%, 14px 100%);
  }
  .date-line { width: 168px; height: 1px; background: var(--rule); margin: 0 0 3px 5px; }
  .backdrop-brand {
    position: absolute; left: 130px; top: 367px; width: 334px;
    text-align: center; color: var(--faint); font-weight: 700;
  }
  .backdrop-mark {
    display: block; width: 110px; height: 110px; margin: 0 auto 18px;
    border-radius: 50%; background: #f3f3f3;
    box-shadow: 0 0 0 4px var(--paper), 0 0 0 5px var(--faint-ring);
  }
  .backdrop-name { display: block; font-size: 52px; line-height: 1; }
  .backdrop-tag {
    display: block; font-size: 21px; letter-spacing: 5.5px;
    margin-top: 10px; text-transform: uppercase;
  }
  .footer-band {
    position: absolute; left: 0; bottom: 0; width: 594px; height: 25px;
    background: var(--red);
  }
</style>
</head>
<body>
<div class="stage">
  <div class="letterhead">
    <svg class="header-shapes" width="594" height="170" viewBox="0 0 594 170" aria-hidden="true">
      <polygon points="236,0 252,0 343,137 330,140" fill="var(--red)"/>
      <polygon points="252,0 594,0 594,137 343,137" fill="var(--orange)"/>
    </svg>

    <div class="brand">
      <span class="brand-mark"></span>
      <span class="brand-name">Sunmark Growth</span>
      <span class="brand-tag">Coaching Services</span>
    </div>

    <address class="contact" style="font-style:normal">
      Daryna Feltwick-Osbourne<br>
      daryna@sunmarkgrowthco.com<br>
      sunmarkgrowthco.com<br>
      REACH US: 555-314-7720
    </address>

    <div class="date-field">
      <span class="date-label">DATE :</span>
      <span class="date-line"></span>
    </div>

    <div class="backdrop-brand" aria-hidden="true">
      <span class="backdrop-mark"></span>
      <span class="backdrop-name">Sunmark Growth</span>
      <span class="backdrop-tag">Coaching Services</span>
    </div>

    <div class="footer-band"></div>
  </div>
</div>
</body>
</html>
```